Valtesh Spinal Care and Performance

We need new business cards, something more modern, clean. On the back of the card maybe a quote. The Dr. likes, “The doctor of the future will give no medicine, but will interest his patient in the care of the human frame, in diet and in the cause and prevention of disease.” - Walter Pimsley. We are open to other suggestions. We are a chiropractic office.

```html
<!DOCTYPE html>
<html lang="en">
<head>
<meta charset="utf-8">
<title>Valtesh Spinal Care and Performance — Business Card</title>
<link href="https://fonts.googleapis.com/css2?family=Poppins:wght@400;500;600&display=swap" rel="stylesheet">
<style>
  :root {
    --plum: #45134b;
    --plum-text: #5a2a63;
    --white: #ffffff;
    --quote-grey: #6b6b6b;
    --backdrop: #d9d9db;
    --line-soft: rgba(255, 255, 255, 0.55);
  }
  * { box-sizing: border-box; margin: 0; padding: 0; }
  html, body {
    width: 1200px;
    height: 800px;
    overflow: hidden;
    background: var(--backdrop);
    font-family: "Poppins", sans-serif;
  }
  .sheet {
    width: 1200px;
    height: 800px;
    display: flex;
    align-items: center;
    justify-content: center;
    gap: 40px;
  }
  .card {
    width: 540px;
    height: 309px;
    border-radius: 22px;
    position: relative;
    overflow: hidden;
    box-shadow: 0 6px 18px rgba(0, 0, 0, 0.18);
  }

  /* Front */
  .card--front {
    background: var(--plum);
    color: var(--white);
  }
  .front-brand {
    position: absolute;
    left: 40px;
    top: 92px;
    width: 230px;
    font-size: 22px;
    font-weight: 500;
    line-height: 1.25;
    letter-spacing: 0.02em;
    color: var(--white);
  }
  .front-divider {
    position: absolute;
    left: 300px;
    top: 46px;
    width: 1px;
    height: 150px;
    background: var(--line-soft);
  }
  .contact {
    position: absolute;
    left: 326px;
    top: 50px;
  }
  .contact__name {
    font-size: 16px;
    font-weight: 600;
    letter-spacing: 0.04em;
    text-transform: uppercase;
    line-height: 1.2;
  }
  .contact__title {
    font-size: 12px;
    font-weight: 500;
    margin-bottom: 10px;
  }
  .contact__list { list-style: none; }
  .contact__item {
    display: flex;
    align-items: center;
    gap: 8px;
    font-size: 12px;
    line-height: 19px;
  }
  .contact__item svg {
    width: 11px;
    height: 11px;
    fill: var(--white);
    flex: none;
  }
  .address {
    position: absolute;
    left: 40px;
    bottom: 30px;
    display: flex;
    align-items: center;
    gap: 8px;
    font-size: 12.5px;
    letter-spacing: 0.02em;
  }
  .address svg { width: 11px; height: 13px; fill: var(--white); }

  /* Back */
  .card--back {
    background: var(--white);
    display: flex;
    flex-direction: column;
    align-items: center;
    justify-content: center;
    padding: 0 40px;
  }
  .back-brand {
    font-size: 23px;
    font-weight: 500;
    color: var(--plum-text);
    letter-spacing: 0.02em;
    text-align: center;
    line-height: 1.25;
    margin-bottom: 36px;
  }
  .quote {
    font-size: 11.5px;
    line-height: 1.55;
    color: var(--quote-grey);
    text-align: center;
  }
</style>
</head>
<body>
<main class="sheet">

  <section class="card card--front" aria-label="Card front">
    <p class="front-brand">Valtesh Spinal Care and Performance</p>
    <span class="front-divider"></span>

    <div class="contact">
      <p class="contact__name">Daniel Corwin</p>
      <p class="contact__title">President</p>
      <ul class="contact__list">
        <li class="contact__item">
          <svg viewBox="0 0 24 24"><path d="M6.6 10.8a15.1 15.1 0 0 0 6.6 6.6l2.2-2.2a1 1 0 0 1 1-.25 11.4 11.4 0 0 0 3.6.57 1 1 0 0 1 1 1V20a1 1 0 0 1-1 1A17 17 0 0 1 3 4a1 1 0 0 1 1-1h3.5a1 1 0 0 1 1 1c0 1.25.2 2.45.57 3.57a1 1 0 0 1-.25 1z"/></svg>
          555-204-7713
        </li>
        <li class="contact__item">
          <svg viewBox="0 0 24 24"><path d="M7 1h10a2 2 0 0 1 2 2v18a2 2 0 0 1-2 2H7a2 2 0 0 1-2-2V3a2 2 0 0 1 2-2zm0 3v14h10V4z"/></svg>
          555-318-6402
        </li>
        <li class="contact__item">
          <svg viewBox="0 0 24 24"><path d="M6 2h9l3 3v4h2a2 2 0 0 1 2 2v9a2 2 0 0 1-2 2H4a2 2 0 0 1-2-2v-9a2 2 0 0 1 2-2h2zm2 2v5h8V6h-2V4zm-2 9v2h3v-2zm5 0v2h3v-2zm5 0v2h3v-2z"/></svg>
          555-427-9150
        </li>
        <li class="contact__item">
          <svg viewBox="0 0 24 24"><path d="M2 4h20v16H2zm2 2v.5l8 5.5 8-5.5V6zm0 3v9h16V9l-8 5.5z"/></svg>
          info@valtesh.com
        </li>
        <li class="contact__item">
          <svg viewBox="0 0 24 24"><path d="M12 2a10 10 0 1 0 0 20 10 10 0 0 0 0-20zm6.9 9h-3a15 15 0 0 0-1.3-5.9A8 8 0 0 1 18.9 11zM12 4.1c.9 1.2 1.7 3.5 1.9 6.9h-3.8c.2-3.4 1-5.7 1.9-6.9zM9.4 5.1A15 15 0 0 0 8.1 11h-3a8 8 0 0 1 4.3-5.9zM5.1 13h3a15 15 0 0 0 1.3 5.9A8 8 0 0 1 5.1 13zm6.9 6.9c-.9-1.2-1.7-3.5-1.9-6.9h3.8c-.2 3.4-1 5.7-1.9 6.9zm2.6-1a15 15 0 0 0 1.3-5.9h3a8 8 0 0 1-4.3 5.9z"/></svg>
          www.valtesh.com
        </li>
      </ul>
    </div>

    <p class="address">
      <svg viewBox="0 0 20 24"><path d="M10 0a8 8 0 0 0-8 8c0 6 8 16 8 16s8-10 8-16a8 8 0 0 0-8-8zm0 11a3 3 0 1 1 0-6 3 3 0 0 1 0 6z"/></svg>
      4120 Larkspur Court Fairbanks, Alaska 99701
    </p>
  </section>

  <section class="card card--back" aria-label="Card back">
    <p class="back-brand">Valtesh Spinal Care and Performance</p>
    <p class="quote">
      The doctor of the future will give no medicine,<br>
      but will interest his patient in the care of the human frame,<br>
      in diet and in the cause and prevention of disease.” – Walter Pimsley.
    </p>
  </section>

</main>
</body>
</html>
```